Pagecraft Design Project - Australian Solar Company wants to start FRESH!

About us

Brightfield Power are a renewable energy company based in Perth Australia, but we also have offices all over Asia. We specialise in offering renewable energy solutions (Solar PV Systems and LED Lighting) to residential and commercial customers.

Our current website: www.brightfieldpower.com.au

Our needs

This will be a replacement website as we are not happy with our current layout. We have an Australian company doing our SEO and they have recommended a new layout which we wish to go with.

We really want a professional and easy to navigate website that will assist in bringing in more enquiries and phone calls.

Content

We have all the content and will get the design winner to add this after we have chosen the design we like.
It is important that the call to actions are presented well and are visible these are things like the free quote form and our phone number.

The layout as we have advised has been based on SEO research so we wish it to be exactly the same unless otherwise stated.

Call to action

Our main objective of the new website is for people to come to the home page and see us as a professional and reliable company to deal with and enquire further.

We really want as many people as we can to convert to a lead. We want every person that comes to the website to enquire online or call us. We feel it is important to have a contact us/quote form on every page of the website.

Functional requirements

We have a friendloop and clipstream account so links to these would be needed

Design assets

The logo needs to be displayed as shown in the website layout brief

Colours – we would like fresh, subdued colours that are professional and appealing to the eye. We ask that you do not take the colours from the logo.

Current website dislikes – the things we currently dislike about our current website is that it is hard to find information and there is no clear call to action. The colours are really unappealing as well as it looks cheap not professional.
The graphics that we require for the slider on the home page will have to be given after the winner is chosen but we want there to be three sliders on rotation

- Credibility builder (employee infront of solar panel) that encourages we use all our own employees not subcontractors
- Residential Slider – picture of a couple and solar panel system with a testimonial
- Commercial slider – picture of commercial system with “find out how you can install solar for free* at your business”

Design ideas

The website needs to be mobile friendly as well
It is going to be a total rebuild from the current website as our current website really isn’t working for us.

Target Market(s)

Target Audience

Our target audience are both residential and commercial clients
Residential – we want to attract home owners that are interested in reducing their electricity bill and helping the environment. Generally these people are between the ages of 28-50+ both male and female.

Commercial – We want to appeal to key decision makers within the commercial sphere. For example – CEOs, Company Directors, Operation managers and business owners of any industry. These people will be interested in reducing their electricity bills and creating a clean green image for their business.
Our target audience will generally come to our website to get information and enquire for a quote/ product information.

Industry/Entity Type

Residential

Requirements
Must have
• MUST BE LAID OUT LIKE THIS:

http://www.docvaultex.com/doc/482937015/Website-Layout

Must have Enquire Now forms on every page that read:

Name
Phone Number
How did you hear about us
Message

```html
<!DOCTYPE html>
<html lang="en">
<head>
<meta charset="utf-8">
<title>Brightfield Power – Contact Us</title>
<link href="https://fonts.googleapis.com/css2?family=Open+Sans:wght@300;400;600;700&family=Roboto:wght@400&display=swap" rel="stylesheet">
<style>
:root{
  --brand-blue:#3b8bd0;
  --link-blue:#3a8fd6;
  --text-dark:#333;
  --text-mid:#555;
  --rule:#ececec;
  --footer-bg:#333333;
  --footer-btn:#5a5a5a;
  --white:#fff;
}
*{box-sizing:border-box;margin:0;padding:0}
html,body{width:1200px;height:1200px;overflow:hidden}
body{font-family:"Open Sans",Arial,sans-serif;color:var(--text-dark);background:var(--white);position:relative}
.topbar{position:absolute;left:0;top:0;width:1200px;height:38px;background:var(--brand-blue);color:#eaf3fb;font-size:11px}
.topbar .item{position:absolute;top:12px;display:flex;align-items:center;gap:5px;white-space:nowrap}
.topbar svg{fill:#fff}
.header{position:absolute;top:38px;left:0;width:1200px;height:115px;background:var(--white)}
.brand{position:absolute;left:86px;top:44px;display:flex;align-items:center;gap:10px}
.brand .dot{width:36px;height:36px;border-radius:50%;background:#e9a91d}
.brand .name{font-size:24px;font-weight:600;color:#2f6fa8}
.nav{position:absolute;top:52px;right:80px;display:flex;gap:44px;font-size:11.5px;text-transform:uppercase;color:#333;white-space:nowrap}
.hero{position:absolute;top:153px;left:0;width:1200px;height:290px;overflow:hidden}
.hero-bg{position:absolute;inset:0;background:linear-gradient(90deg,#b9c7d9 0%,#6f93bd 20%,#4d7fb3 38%,#6d9ac6 60%,#c8d3e0 85%,#8fa9c6 100%)}
.hero h1{position:absolute;left:462px;top:0;font-size:44px;font-weight:700;color:var(--white);letter-spacing:-.5px;line-height:56px}
.field{position:absolute;background:#fff;border:1px solid #d8dee6;border-radius:3px;font-size:12.5px;color:#999;padding:9px 8px;white-space:nowrap;overflow:hidden}
.sum{position:absolute;left:651px;top:240px;color:#fff;font-size:25px;font-weight:600}
.submit{position:absolute;left:920px;top:240px;width:83px;height:35px;background:linear-gradient(#3e8fd4,#2c73b7);color:#fff;font-family:Roboto,Arial,sans-serif;font-size:14px;border-radius:3px;text-align:center;line-height:33px}
.slider-dots{position:absolute;left:50%;bottom:12px;transform:translateX(-50%);display:flex;gap:8px}
.slider-dots span{width:8px;height:8px;border-radius:50%;background:rgba(255,255,255,.5)}
.slider-dots span.active{background:#fff}
.services{position:absolute;top:443px;left:0;width:1200px}
.service{position:absolute;top:0;width:340px}
.service svg{position:absolute;top:26px}
.service .label{position:absolute;top:100px;white-space:nowrap;font-size:17.8px;color:var(--link-blue)}
.service .label::before{content:"+";color:#aaa;font-size:14px;margin-right:10px;position:relative;top:-2px}
.divider{position:absolute;top:600px;left:81px;width:1039px;height:1px;background:var(--rule)}
.welcome{position:absolute;left:81px;top:642px;font-size:28px;font-weight:300;color:var(--link-blue);white-space:nowrap}
.welcome small{font-size:11px;color:#555;text-transform:uppercase;margin-left:6px}
.post{position:absolute;left:81px;width:510px}
.date{position:absolute;left:0;top:0;width:45px;height:63px;border:1px solid #e6e6e6;border-radius:4px;text-align:center}
.date .day{font-size:26px;font-weight:300;color:var(--link-blue);line-height:46px}
.date .mon{position:absolute;bottom:0;left:0;right:0;height:17px;background:var(--brand-blue);color:#fff;font-size:11px;line-height:17px}
.post h3{position:absolute;left:66px;top:2px;font-size:16px;font-weight:400;color:#333;white-space:nowrap}
.post .meta{position:absolute;left:66px;top:30px;font-size:11px;color:#666}
.post p{position:absolute;left:66px;top:50px;width:440px;font-size:11.5px;line-height:19px;color:var(--text-mid)}
.post p b{font-weight:600;color:#333}
.video{position:absolute;left:614px;top:634px;width:506px;height:323px;background:#111}
.video .frame{position:absolute;left:0;top:30px;width:506px;height:282px;background:linear-gradient(135deg,#6f6e69 0%,#9ea39f 40%,#4f6d96 60%,#7b7a74 100%)}
.video .title{position:absolute;left:11px;top:8px;color:#eee;font-family:Roboto,Arial,sans-serif;font-size:12px}
.video .play{position:absolute;left:219px;top:136px;width:70px;height:50px;border-radius:10px;background:rgba(20,20,20,.8)}
.footer{position:absolute;top:1038px;left:0;width:1200px;height:162px;background:var(--footer-bg)}
.fbtn{position:absolute;top:62px;height:32px;padding:0 17px;background:var(--footer-btn);border:1px solid #6b6b6b;border-radius:2px;color:#f0f0f0;font-size:12.5px;line-height:30px;white-space:nowrap}
</style>
</head>
<body>
<div class="topbar">
  <div class="item" style="left:649px"><svg width="13" height="11" viewBox="0 0 13 11"><path d="M6.5 0 13 5.5h-2V11H8V7.5H5V11H2V5.5H0z"/></svg>Your company location</div>
  <div class="item" style="left:816px"><svg width="11" height="11" viewBox="0 0 11 11"><path d="M2 0l2 2.5-1.2 1.5a7 7 0 0 0 4.2 4.2L8.5 7 11 9l-1.5 2C4.5 11 0 6.5 0 1.5z"/></svg>(+61) 000-0001</div>
  <div class="item" style="left:940px"><svg width="14" height="10" viewBox="0 0 14 10"><path d="M0 0h14v10H0zM1 1l6 4.5L13 1z"/></svg>example@yourmail.com</div>
  <div class="item" style="left:1098px">friendloop</div>
</div>

<header class="header">
  <div class="brand"><span class="dot"></span><span class="name">Brightfield Power</span></div>
  <nav class="nav"><span>About Us</span><span>Products</span><span>Services</span><span>Why Brightfield Power</span><span>Contact</span></nav>
</header>

<section class="hero">
  <div class="hero-bg" role="img" aria-label="Rotating slider photo: blurred city street with a hand holding a smartphone on the left"></div>
  <h1>Contact Us</h1>
  <div class="field" style="left:468px;top:61px;width:170px;height:35px">Name *</div>
  <div class="field" style="left:653px;top:61px;width:170px;height:35px">Phone Number *</div>
  <div class="field" style="left:836px;top:61px;width:169px;height:35px">How did you hear about us</div>
  <div class="field" style="left:468px;top:108px;width:536px;height:122px">Message</div>
  <div class="field" style="left:470px;top:241px;width:171px;height:35px">Enter sum</div>
  <div class="sum">9+1</div>
  <div class="submit">Submit</div>
  <div class="slider-dots"><span class="active"></span><span></span><span></span></div>
</section>

<section class="services">
  <div class="service" style="left:114px">
    <svg style="left:130px" width="34" height="34" viewBox="0 0 34 34"><circle cx="17" cy="17" r="13" fill="none" stroke="#2f97e6" stroke-width="5" stroke-dasharray="3 2.2"/><circle cx="17" cy="17" r="10" fill="#2f97e6"/><circle cx="17" cy="17" r="7" fill="#43a6ef"/></svg>
    <div class="label">Perth Residential Solar Power</div>
  </div>
  <div class="service" style="left:468px">
    <svg style="left:130px" width="36" height="36" viewBox="0 0 36 36" fill="#3c8fd6"><circle cx="18" cy="18" r="6" fill="none" stroke="#3c8fd6" stroke-width="3"/><circle cx="18" cy="3" r="2"/><circle cx="18" cy="33" r="2"/><circle cx="3" cy="18" r="2"/><circle cx="33" cy="18" r="2"/><circle cx="7.5" cy="7.5" r="2"/><circle cx="28.5" cy="28.5" r="2"/><circle cx="28.5" cy="7.5" r="2"/><circle cx="7.5" cy="28.5" r="2"/></svg>
    <div class="label">Perth Commercial Solar Power</div>
  </div>
  <div class="service" style="left:823px">
    <svg style="left:76px" width="36" height="36" viewBox="0 0 36 36"><path d="M18 3A15 15 0 1 1 3.5 22" fill="none" stroke="#3c8fd6" stroke-width="4"/><path d="M18 33A15 15 0 0 1 6 9" fill="none" stroke="#1f5f9c" stroke-width="4"/></svg>
    <div class="label">Perth LED Lightning</div>
  </div>
</section>

<div class="divider"></div>

<h2 class="welcome">Welcome<small>Latest News</small></h2>

<article class="post" style="top:701px">
  <div class="date"><div class="day">01</div><div class="mon">AUG</div></div>
  <h3>Australia to move ahead with massive solar</h3>
  <div class="meta">admin-solar &nbsp; Aug 1, 2013</div>
  <p>Australia to move ahead with massive solar project by Staff Writers Sydney (NWS) Jul 31, 2013 A $403 million solar power project in Australia, touted as the Southern... <b>Read More ›</b></p>
</article>

<article class="post" style="top:839px">
  <div class="date"><div class="day">30</div><div class="mon">JUL</div></div>
  <h3>China takes axe to polysilicon producers</h3>
  <div class="meta">admin-solar &nbsp; Jul 30, 2013</div>
  <p>China takes axe to polysilicon producers as solar panels pile up Demand for solar panels has eased since the global financial crisis, leaving the industry sitting on idle capacity... <b>Read More ›</b></p>
</article>

<div class="video">
  <div class="frame" role="img" aria-label="Video still of a client testimonial filmed in a workshop"></div>
  <div class="title">Harbor Video Production - Client Testimonial Sa...</div>
  <div class="play"><svg width="70" height="50" viewBox="0 0 70 50"><path d="M28 15l16 10-16 10z" fill="#fff"/></svg></div>
</div>

<footer class="footer">
  <div class="fbtn" style="left:81px">Primary Prod. /Services</div>
  <div class="fbtn" style="left:348px">Memberships</div>
  <div class="fbtn" style="left:614px">Request Quotation</div>
  <div class="fbtn" style="left:880px">Contact Info.</div>
</footer>
</body>
</html>
```